Etiketten für Honiggläser
Zielgruppe
Ich bin ein Imker und möchte meinen Honig verkaufen.
Aufgabenstellung
Ich möchte exklusive und edle Honigetiketten die auffallen. Ich habe weder ein Logo noch hat meine Imkerei einen Namen. ( Vorschläge sind aber auch willkommen ).
Auf die Vorderseite des Honigetiketts soll zu lesen sein:
- Deutscher Honig
- Art des Honigs: Blütenhonig / Waldhonig ...
- 500g
Auf der Rückseite des Honigetiketts soll zu finden sein:
- Namen und Adresse des Imkers
- freies Feld für das Mindesthaltbarkeitsdatum
Ergänzende Informationen:
- Name: Tobias Wend
- Adresse: Lindauer Gasse 47, 85399 Eggmoos ( Bayern )
Bitte in einem Format liefern, dass ich ohne Aufwände an eine Druckerei übergeben kann. Außerdem muss ich die Dateien bearbeiten können in Photoshop o.ä. um zB die Art des Honigs und die Füllmenge anpassen zu können.
Wichtig:
Die Abmessungen des Labels sollen 15,5cm - 17cm breit und 6cm hoch sein.

```html
<!DOCTYPE html>
<html lang="de">
<head>
<meta charset="utf-8">
<title>Blütenhonig Etikett</title>
<link href="https://fonts.googleapis.com/css2?family=Caveat:wght@400;600&family=Jost:wght@400&display=swap" rel="stylesheet">
<style>
  :root {
    --page: #ffffff;
    --label-black: #000000;
    --text-light: #ffffff;
    --honey-gold: #fbc640;
    --honey-amber: #f7931e;
    --honey-orange: #f05a1a;
    --honey-red: #d9121f;
    --honey-peach: #f6a97a;
  }
  html, body {
    margin: 0;
    padding: 0;
    width: 1200px;
    height: 1200px;
    overflow: hidden;
    background: var(--page);
  }
  .label-strip {
    position: absolute;
    left: 25px;
    top: 390px;
    width: 1150px;
    height: 420px;
    display: flex;
    gap: 2px;
  }
  .panel {
    position: relative;
    height: 100%;
    background: var(--label-black);
    overflow: hidden;
  }
  .panel--back-left { width: 300px; }
  .panel--front { width: 544px; }
  .panel--back-right { width: 302px; }

  .drip-band {
    position: absolute;
    left: 0; right: 0; top: 0;
    height: 110px;
  }
  .comb-band {
    position: absolute;
    left: 0; right: 0; bottom: 0;
    height: 95px;
  }
  .panel--back-left .drip-band {
    background: linear-gradient(90deg, var(--honey-peach) 0%, var(--honey-orange) 25%, var(--honey-gold) 50%, var(--honey-gold) 75%, var(--honey-amber) 100%);
  }
  .panel--back-left .comb-band {
    background: linear-gradient(90deg, var(--honey-peach) 0%, var(--honey-orange) 40%, var(--honey-gold) 80%, var(--honey-amber) 100%);
  }
  .panel--front .drip-band {
    background: linear-gradient(90deg, var(--honey-amber) 0%, var(--honey-gold) 25%, var(--honey-amber) 50%, var(--honey-red) 70%, var(--honey-orange) 100%);
  }
  .panel--front .comb-band {
    background: linear-gradient(90deg, var(--honey-red) 0%, var(--honey-orange) 25%, var(--honey-gold) 45%, var(--honey-red) 65%, var(--honey-amber) 100%);
  }
  .panel--back-right .drip-band {
    background: linear-gradient(90deg, var(--honey-red) 0%, var(--honey-orange) 45%, var(--honey-red) 100%);
  }
  .panel--back-right .comb-band {
    background: linear-gradient(90deg, var(--honey-amber) 0%, var(--honey-orange) 50%, var(--honey-red) 100%);
  }

  .address {
    position: absolute;
    left: 96px;
    top: 176px;
    margin: 0;
    font-family: "Jost", sans-serif;
    font-size: 14px;
    line-height: 20px;
    color: var(--text-light);
    font-style: normal;
  }

  .product-title {
    position: absolute;
    left: 0; right: 0;
    top: 145px;
    margin: 0;
    text-align: center;
    color: var(--text-light);
    font-weight: normal;
  }
  .product-title__kind {
    position: absolute;
    left: 253px;
    top: 0;
    font-family: "Caveat", cursive;
    font-size: 30px;
    line-height: 1;
  }
  .product-title__name {
    position: absolute;
    left: 200px;
    top: 14px;
    font-family: "Caveat", cursive;
    font-weight: 600;
    font-size: 104px;
    line-height: 1;
    letter-spacing: -1px;
  }
  .origin {
    position: absolute;
    left: 200px;
    top: 260px;
    margin: 0;
    font-family: "Jost", sans-serif;
    font-size: 15px;
    color: var(--text-light);
  }
  .net-weight {
    position: absolute;
    left: 0; right: 0;
    top: 293px;
    margin: 0;
    text-align: center;
    font-family: "Jost", sans-serif;
    font-size: 22px;
    color: var(--text-light);
  }

  .storage-note {
    position: absolute;
    left: 0;
    top: 200px;
    margin: 0;
    padding-left: 0;
    font-family: "Jost", sans-serif;
    font-size: 10px;
    line-height: 16px;
    color: var(--text-light);
  }
</style>
</head>
<body>
  <main class="label-strip">
    <section class="panel panel--back-left">
      <div class="drip-band" role="img" aria-label="Honey drips running down in gold and orange tones"></div>
      <address class="address">Tobias Wend<br>Lindauer Gasse 47<br>85399 Eggmoos (Bayern)</address>
      <div class="comb-band" role="img" aria-label="Honeycomb cells in peach, orange and gold tones"></div>
    </section>

    <section class="panel panel--front">
      <div class="drip-band" role="img" aria-label="Honey drips running down in gold, orange and red tones"></div>
      <h1 class="product-title">
        <span class="product-title__kind">Blüten-</span>
        <span class="product-title__name">Honig</span>
      </h1>
      <p class="origin">aus Deutschland</p>
      <p class="net-weight">500g</p>
      <div class="comb-band" role="img" aria-label="Honeycomb cells in red, orange and gold tones"></div>
    </section>

    <section class="panel panel--back-right">
      <div class="drip-band" role="img" aria-label="Honey drips running down in red and orange tones"></div>
      <p class="storage-note">Trocken und vor Wärme geschützt lagern<br>Mindestens haltbar bis</p>
      <div class="comb-band" role="img" aria-label="Honeycomb cells in orange and red tones"></div>
    </section>
  </main>
</body>
</html>
```